Dorsey K. Wendell Business Card

We need a business card for our company Dorsey K. Wendell Heating & Plumbing to be distributed to potential customers. It should follow the color scheme of our logo and have a modern upscale and masculine look.

The logo is attached and the info below should also be included:

5187 W. Cedar Brook Rd.
Hollister, PA 17583

Russell T. Wendell
(717) 592-0817
russelltwendell@fernmail.net
dorseykwendell.net
PA #093148

Industry/Entity Type

Business

Contact Information for Business Card

5187 W. Cedar Brook Rd.
Hollister, PA 17583

Russell T. Wendell
(717) 592-0817
russelltwendell@fernmail.net
dorseykwendell.net
PA #093148

Colors

Designer to choose colors to be used in the design.

Requirements
Must have
• Information above included

```html
<!DOCTYPE html>
<html lang="en">
<head>
<meta charset="utf-8">
<title>Dorsey K. Wendell Business Card</title>
<link rel="stylesheet" href="https://fonts.googleapis.com/css2?family=Roboto:wght@400&family=Roboto+Condensed:wght@700&display=swap">
<style>
  :root {
    --brand-blue: #0b56a4;
    --card-white: #f1f1f1;
    --ink-grey: #555555;
    --backdrop: #2a2a2a;
    --paper-edge: #d9d9d9;
  }
  * { margin: 0; padding: 0; box-sizing: border-box; }
  html, body { width: 1200px; height: 960px; overflow: hidden; }
  body {
    background: var(--backdrop);
    position: relative;
    font-family: "Roboto", Arial, sans-serif;
  }
  .card {
    position: absolute;
    width: 600px;
    height: 343px;
    border-radius: 22px;
    overflow: hidden;
  }
  .card--back {
    left: 322px; top: 107px;
    background: var(--brand-blue);
  }
  .back-mark {
    position: absolute;
    left: 0; right: 0; top: 118px;
    display: flex; align-items: center; justify-content: center; gap: 14px;
  }
  .back-mark__square {
    width: 30px; height: 30px; background: #ffffff;
  }
  .back-mark__name {
    font-family: "Roboto Condensed", Arial, sans-serif;
    font-weight: 700;
    font-size: 40px;
    letter-spacing: 0.5px;
    color: #ffffff;
    text-transform: uppercase;
  }
  .back-url {
    position: absolute;
    left: 0; right: 0; top: 293px;
    text-align: center;
    color: #ffffff;
    font-size: 14px;
    letter-spacing: 1.6px;
  }
  .card--front {
    left: 320px; top: 493px;
    background: var(--card-white);
    box-shadow: inset 0 0 0 1px var(--paper-edge);
  }
  .brand-lockup {
    position: absolute;
    left: 33px; top: 30px;
    display: flex; align-items: center; gap: 9px;
  }
  .brand-lockup__square {
    width: 20px; height: 20px; background: var(--brand-blue);
  }
  .brand-lockup__name {
    font-family: "Roboto Condensed", Arial, sans-serif;
    font-weight: 700;
    font-size: 22px;
    line-height: 1.05;
    color: var(--brand-blue);
    text-transform: uppercase;
  }
  .feature-panel {
    position: absolute;
    left: 301px; top: 19px;
    width: 281px; height: 281px;
    background: var(--brand-blue);
  }
  .contact {
    position: absolute;
    left: 33px; top: 151px;
    color: var(--ink-grey);
    font-size: 14.5px;
    line-height: 18px;
  }
  .contact__name {
    font-family: "Roboto Condensed", Arial, sans-serif;
    font-weight: 700;
    font-size: 21px;
    color: var(--brand-blue);
    text-transform: uppercase;
    margin-bottom: 12px;
    line-height: 26px;
  }
  .contact__address { margin-bottom: 10px; }
  .contact__row { display: flex; align-items: center; gap: 8px; height: 19.5px; }
  .contact__row svg { width: 14px; height: 14px; fill: var(--brand-blue); flex: none; }
  .contact__license { margin-top: 2px; }
</style>
</head>
<body>
  <section class="card card--back" aria-label="Business card back">
    <div class="back-mark">
      <span class="back-mark__square"></span>
      <span class="back-mark__name">Dorsey K. Wendell</span>
    </div>
    <p class="back-url">www.dorseykwendell.net</p>
  </section>

  <section class="card card--front" aria-label="Business card front">
    <div class="brand-lockup">
      <span class="brand-lockup__square"></span>
      <span class="brand-lockup__name">Dorsey K. Wendell<br>Heating &amp; Plumbing</span>
    </div>

    <div class="contact">
      <h1 class="contact__name">Russell T. Wendell</h1>
      <p class="contact__address">5187 W. Cedar Brook Rd.<br>Hollister, PA 17583</p>
      <p class="contact__row">
        <svg viewBox="0 0 24 24" aria-hidden="true"><path d="M6.6 10.8a15.1 15.1 0 0 0 6.6 6.6l2.2-2.2c.3-.3.7-.4 1-.2 1.1.4 2.3.6 3.6.6.6 0 1 .4 1 1V20c0 .6-.4 1-1 1A17 17 0 0 1 3 4c0-.6.4-1 1-1h3.5c.6 0 1 .4 1 1 0 1.3.2 2.5.6 3.6.1.3 0 .7-.2 1z"/></svg>
        (717) 592-0817
      </p>
      <p class="contact__row">
        <svg viewBox="0 0 24 24" aria-hidden="true"><path d="M2 5h20v14H2z M3.5 6.5 12 13l8.5-6.5" fill="none" stroke="#0b56a4" stroke-width="2.4"/></svg>
        russelltwendell@fernmail.net
      </p>
      <p class="contact__row">
        <svg viewBox="0 0 24 24" aria-hidden="true"><circle cx="12" cy="12" r="10"/><path d="M2 12h20M12 2c3 3 3 17 0 20M12 2c-3 3-3 17 0 20" fill="none" stroke="#f1f1f1" stroke-width="1.6"/></svg>
        dorseykwendell.net
      </p>
      <p class="contact__license">PA #093148</p>
    </div>

    <div class="feature-panel" aria-hidden="true"></div>
  </section>
</body>
</html>
```